Launching new podcast and need artwork

we are two guys in our early 40's from east Texas who are starting a podcast around personal finance.

The title of the podcast will be "Ledger Gripes" and the subtitle will be "Financial hacks with some southern charm"

We own the company boundlessdaysplanning.example and will be using the podcast as a lead generation for our primary business of financial coaching.

Target Market(s)

Male 35-45 years old

Industry/Entity Type

Personal finance

Requirements
Nice to have
• Rugged or rustic feel would fit our personas

```html
<!DOCTYPE html>
<html lang="en">
<head>
<meta charset="utf-8">
<title>Ledger Gripes – Podcast Cover</title>
<link href="https://fonts.googleapis.com/css2?family=Bebas+Neue&display=swap" rel="stylesheet">
<style>
  :root {
    --backdrop: #cbcbcb;
    --charcoal: #231e1c;
    --rust: #a8361a;
    --flame: #ff3d00;
    --white: #ffffff;
  }
  html, body {
    margin: 0;
    padding: 0;
    overflow: hidden;
  }
  body {
    width: 1183px;
    height: 1200px;
    background: var(--backdrop);
    position: relative;
    font-family: "Bebas Neue", "Oswald", sans-serif;
  }
  .cover {
    position: absolute;
    left: 153px;
    top: 153px;
    width: 876px;
    height: 876px;
    background: var(--charcoal);
    overflow: hidden;
  }
  .rustic-band {
    position: absolute;
    left: 0;
    top: 30px;
    width: 100%;
    height: 376px;
    background: linear-gradient(180deg,
      #6e2716 0%, var(--rust) 22%, var(--rust) 78%, #6e2716 100%);
  }
  .tagline {
    position: absolute;
    left: 0;
    width: 100%;
    text-align: center;
    color: var(--white);
    margin: 0;
    font-weight: 400;
    line-height: 1;
  }
  .tagline-lead {
    top: 133px;
    font-size: 62px;
    letter-spacing: 1px;
  }
  .tagline-main {
    top: 205px;
    font-size: 124px;
    letter-spacing: 2px;
  }
  .show-name {
    position: absolute;
    left: 0;
    top: 478px;
    width: 100%;
    margin: 0;
    text-align: center;
    color: var(--flame);
    font-size: 150px;
    font-weight: 400;
    line-height: 0.95;
    letter-spacing: 4px;
  }
</style>
</head>
<body>
  <main class="cover">
    <div class="rustic-band" role="img" aria-label="Distressed rust-orange wood grain texture band"></div>
    <p class="tagline tagline-lead">Financial hacks with some</p>
    <p class="tagline tagline-main">Southern Charm</p>
    <h1 class="show-name">Ledger<br>Gripes</h1>
  </main>
</body>
</html>
```